Life and Personal development life coach needs card design

I need a card design that matches the style and design of my website. I'd like to stay in the same color scheme. Please check out my website for ideas. www.bretamoorvale.com
I have had previous designs for this. I am wondering if you have access to those for more ideas??

```html
<!DOCTYPE html>
<html lang="en">
<head>
<meta charset="utf-8">
<title>Life Coach Business Card</title>
<link rel="stylesheet" href="https://fonts.googleapis.com/css2?family=Amatic+SC:wght@400;700&display=swap">
<style>
  :root {
    --page-bg: #e6e6e6;
    --card-pink: #ec86a9;
    --card-blush: #ddb3a3;
    --card-green: #b5d68e;
    --card-mint: #9ed8a0;
    --card-blue: #4fc4e6;
    --ink: #1f1f1f;
    --hand-white: #fbfbf7;
    --hand-blue: #cfe8f4;
    --hand-pink: #f3b3cd;
    --hand-green: #a9dca4;
  }
  * { box-sizing: border-box; margin: 0; padding: 0; }
  html, body {
    width: 1200px;
    height: 750px;
    overflow: hidden;
    background: var(--page-bg);
  }
  .business-card {
    position: absolute;
    left: 60px;
    top: 73px;
    width: 1080px;
    height: 604px;
    overflow: hidden;
    background: linear-gradient(90deg,
      var(--card-pink) 0%,
      var(--card-blush) 18%,
      var(--card-green) 45%,
      var(--card-mint) 78%,
      var(--card-blue) 90%,
      var(--card-blue) 100%);
    box-shadow: 0 2px 10px rgba(0, 0, 0, 0.15);
  }
  .contact-list {
    position: absolute;
    left: 112px;
    top: 40px;
    list-style: none;
    font-family: "Amatic SC", "Arial Narrow", sans-serif;
    font-weight: 400;
    font-size: 58px;
    line-height: 68px;
    letter-spacing: 4px;
    color: var(--ink);
  }
  .hand-illustration {
    position: absolute;
    border-radius: 40px;
    opacity: 0.9;
  }
  .hand-illustration--reaching-right {
    left: 0;
    top: 448px;
    width: 440px;
    height: 126px;
    background: linear-gradient(90deg,
      var(--hand-pink) 0%,
      var(--hand-white) 25%,
      var(--hand-blue) 60%,
      var(--hand-pink) 100%);
    border-radius: 0 60px 60px 0;
  }
  .hand-illustration--reaching-left {
    left: 680px;
    top: 410px;
    width: 400px;
    height: 124px;
    background: linear-gradient(90deg,
      var(--hand-green) 0%,
      var(--hand-blue) 35%,
      var(--hand-white) 75%,
      var(--hand-white) 100%);
    border-radius: 60px 0 0 60px;
  }
</style>
</head>
<body>
  <main class="business-card">
    <ul class="contact-list">
      <li class="contact-list__item">Name</li>
      <li class="contact-list__item">Adress</li>
      <li class="contact-list__item">Phone</li>
      <li class="contact-list__item">Email</li>
    </ul>
    <div class="hand-illustration hand-illustration--reaching-right" role="img" aria-label="Hand-drawn white hand reaching in from the left with pink and blue watercolour wash"></div>
    <div class="hand-illustration hand-illustration--reaching-left" role="img" aria-label="Hand-drawn white hand reaching in from the right with green and blue watercolour wash"></div>
  </main>
</body>
</html>
```